General Dental Office Business Card

I run a private general dental office in southern California, and would like a refresh/redesign of my business card. I focus on quality care rather than volume. The email address on the uploaded current card should be updated to: info@marbleshoredental.example. The current card's logo is a deboss, but I am open to other ideas. The logo can be refreshed, but it is something that's been with me since the beginning of the office, so I wouldn't want a drastic redesign.
Target Market(s)
Adults 18-99, whoever needs dental services
Industry/Entity Type
Healthcare/Dental
Contact Information for Business Card
Name, Address, Phone, email
Colors
Designer to choose colors to be used in the design.
Requirements
Must have
- Logo (Same as original one in the uploaded file), space on back for appointment time/date

```html
<!DOCTYPE html>
<html lang="en">
<head>
<meta charset="utf-8">
<title>Marble Shore Dental – Business Card</title>
<link href="https://fonts.googleapis.com/css2?family=Lato:wght@400;700&family=Montserrat:wght@600&display=swap" rel="stylesheet">
<style>
  :root {
    --sky: #86d3ea;
    --white: #ffffff;
    --mist: #eeeff1;
    --ink: #555a5e;
    --backdrop: #2a2b2d;
  }
  html, body {
    margin: 0;
    width: 1200px;
    height: 952px;
    overflow: hidden;
    background: var(--backdrop);
  }
  .card {
    position: absolute;
    left: 250px;
    width: 700px;
    height: 400px;
    background: var(--white);
    overflow: hidden;
    box-shadow: 0 10px 30px rgba(0,0,0,.45);
  }
  .card--front { top: 56px; }
  .card--back { top: 496px; }
  .card svg.waves { position: absolute; inset: 0; }

  .identity { position: absolute; left: 48px; top: 32px; font-family: "Lato", sans-serif; color: var(--ink); }
  .identity__name {
    margin: 0;
    font-family: "Montserrat", sans-serif;
    font-weight: 600;
    font-size: 26px;
    letter-spacing: .5px;
    color: var(--sky);
  }
  .identity__title { margin: 4px 0 0; font-size: 14px; }
  .identity__rule { width: 30px; height: 2px; background: var(--sky); margin: 10px 0 14px; }
  .identity__address { margin: 0 0 10px; font-size: 12.5px; line-height: 1.45; }
  .contact-list { list-style: none; margin: 0; padding: 0; font-size: 12.5px; line-height: 1.6; }
  .contact-list li { display: flex; align-items: center; gap: 7px; }
  .contact-list svg { width: 11px; height: 11px; fill: var(--sky); }

  .appointment { position: absolute; left: 150px; top: 56px; font-family: "Lato", sans-serif; font-size: 13px; color: var(--ink); }
  .appointment__field { display: flex; align-items: baseline; margin-bottom: 24px; }
  .appointment__line { display: inline-block; border-bottom: 1px dashed #777; margin-left: 4px; }
  .appointment__field--date .appointment__line { width: 360px; }
  .appointment__field--time .appointment__line { width: 420px; }

  .brand {
    position: absolute;
    left: 56px;
    bottom: 38px;
    margin: 0;
    font-family: "Lato", sans-serif;
    font-weight: 400;
    font-size: 36px;
    color: var(--white);
  }
</style>
</head>
<body>

<section class="card card--front" aria-label="Business card front">
  <svg class="waves" viewBox="0 0 700 400" aria-hidden="true">
    <path fill="var(--sky)" d="M0,250 C90,258 140,290 220,300 C300,310 350,334 430,346 C510,358 570,382 640,400 L0,400 Z"/>
    <path fill="none" stroke="var(--white)" stroke-width="7" d="M0,268 C90,276 140,308 220,318 C300,328 350,352 430,364 C510,376 560,396 610,412"/>
    <path fill="none" stroke="var(--white)" stroke-width="7" d="M0,288 C90,296 140,328 220,338 C300,348 350,372 430,384 C480,392 520,404 560,414"/>
  </svg>
  <div class="identity">
    <h1 class="identity__name">DANIEL R. MORENO DDS</h1>
    <p class="identity__title">General Dentistry</p>
    <div class="identity__rule"></div>
    <p class="identity__address">2150 Coral Crest Avenue<br>Seaview, CA 92000</p>
    <ul class="contact-list">
      <li><svg viewBox="0 0 12 12"><path d="M2.5 0.5l2 2.5-1.2 1.3c.7 1.6 2 2.9 3.5 3.6l1.3-1.2 2.5 2-1.3 2C5.5 10.3 1.7 6.5.6 1.8z"/></svg>555-014-2828</li>
      <li><svg viewBox="0 0 12 12"><path d="M0 2h12v8H0z M0 2l6 4 6-4" stroke="var(--white)" stroke-width=".8"/></svg>info@marbleshoredental.example</li>
      <li><svg viewBox="0 0 12 12"><circle cx="6" cy="6" r="5.5"/><path d="M.5 6h11M6 .5c-2.5 3-2.5 8 0 11M6 .5c2.5 3 2.5 8 0 11" stroke="var(--white)" stroke-width=".8" fill="none"/></svg>www.marbleshoredental.example</li>
    </ul>
  </div>
</section>

<section class="card card--back" aria-label="Business card back">
  <svg class="waves" viewBox="0 0 700 400" aria-hidden="true">
    <path fill="none" stroke="var(--mist)" stroke-width="9" d="M30,130 C110,150 150,200 230,215 C310,230 340,270 420,300 C500,330 560,350 640,370"/>
    <path fill="none" stroke="var(--mist)" stroke-width="9" d="M50,115 C130,135 170,185 250,200 C330,215 360,255 440,285 C520,315 580,335 660,355"/>
    <path fill="none" stroke="var(--mist)" stroke-width="9" d="M70,100 C150,120 190,170 270,185 C350,200 380,240 460,270 C540,300 600,320 680,340"/>
    <path fill="var(--sky)" d="M0,150 C60,160 110,200 190,230 C270,255 300,300 380,330 C460,355 540,380 620,400 L0,400 Z"/>
    <circle cx="520" cy="290" r="100" fill="var(--white)"/>
    <circle cx="520" cy="290" r="86" fill="var(--sky)"/>
  </svg>
  <div class="appointment">
    <div class="appointment__field appointment__field--date">Appointment Date<span class="appointment__line"></span></div>
    <div class="appointment__field appointment__field--time">Time<span class="appointment__line"></span></div>
  </div>
  <p class="brand">Marble Shore Dental</p>
</section>

</body>
</html>
```